Villa Sereno needs a new website for its boutique apartment

We are a boutique apartment in Florence that rents out to tourists. We are looking to redesign our website. See the existing site at www.villaserenostay.example

Ideally redesigned site would enable us to easily add and change photos in the gallery and across the site.

The new logo for the apartment is currently under design but being based around the current house logo with a person standing inside.
Updates

Project Deadline Extended
Reason: The website design by the 1st Place designer has been long and drawn out and not led to the design that we were looking for. As such, we are extending the deadline for another 5 days to hopefully get new designs and options.

Target Market(s)

Global tourists

Industry/Entity Type

Accommodation

Coding

Coded - Design and coding required

Number of Pages Required

5+ page

Font styles to use
Sans Serif

Requirements
Must have
• Welcome page, gallery page, information page about apartment and availability page with link to booking sites. And option for another page with tourist information. We must be able to change the photos in the gallery with relative ease when required.
• The Villa Sereno font has been uploaded which is used with the logo and the new logo has been uploaded.
Nice to have
• Looking like a fun but professional hotel site
• Page info is located on www.villaserenostay.example site

```html
<!DOCTYPE html>
<html lang="en">
<head>
<meta charset="utf-8">
<title>Villa Sereno – Boutique Apartment in Florence</title>
<link rel="stylesheet" href="https://fonts.googleapis.com/css2?family=Raleway:wght@300;400;500;600;700&family=Montserrat:wght@400;600;700&display=swap">
<style>
:root{
  --ink:#1f1f1f;
  --muted:#8a8a8a;
  --white:#ffffff;
  --panel-soft:rgba(255,255,255,.38);
  --field:#d9d9d9;
  --footer:#1c1c1c;
  --quote:#9a9a9a;
}
*{box-sizing:border-box;margin:0;padding:0}
html,body{width:1200px;height:2605px;overflow:hidden;background:var(--white)}
body{font-family:"Raleway",sans-serif;color:var(--ink);position:relative}

/* header */
.site-header{position:absolute;left:0;top:0;width:1200px;height:146px;background:var(--white);z-index:3}
.brand{position:absolute;left:80px;top:56px;display:flex;align-items:center;gap:12px;font-family:"Raleway",sans-serif;font-weight:500;font-size:27px;letter-spacing:.5px;color:var(--ink)}
.brand-mark{width:18px;height:18px;border:2px solid var(--ink)}
.main-nav{position:absolute;top:54px;left:417px;display:flex}
.main-nav a{font-family:"Raleway",sans-serif;font-size:19px;color:var(--ink);text-decoration:none;height:40px;line-height:38px;padding:0 18px;border:1.5px solid transparent;margin-right:12px}
.main-nav a.active{border-color:var(--ink)}

/* hero */
.hero{position:absolute;left:0;top:146px;width:1200px;height:714px}
.hero-photo{position:absolute;inset:0;background:
  radial-gradient(ellipse at 78% 30%,#e9dfb0 0%,#b8a56a 18%,transparent 40%),
  radial-gradient(ellipse at 72% 75%,#eef0f8 0%,#c9cde0 25%,transparent 50%),
  linear-gradient(100deg,#7c8a86 0%,#5a5a4a 30%,#3d3424 55%,#6b6550 80%,#4a4030 100%)}
.hero-cut{position:absolute;left:0;top:0;width:1200px;height:714px}
.booking{position:absolute;left:78px;top:0;width:334px;height:471px;background:var(--panel-soft);padding:30px 0 0 36px}
.booking h2{font-weight:400;font-size:35px;color:var(--ink);margin-left:12px;margin-bottom:34px}
.field-label{font-size:16px;color:var(--ink);margin-bottom:4px}
.date-field{width:260px;height:34px;background:var(--field);border:1.5px solid #777;display:flex;align-items:center;justify-content:space-between;padding:0 8px 0 10px;font-family:"Montserrat",sans-serif;font-size:15px;margin-bottom:40px}
.counts{display:flex;gap:50px;margin-top:-12px}
.count-field{width:106px;height:34px;background:var(--field);border:1.5px solid #777;display:flex;align-items:center;justify-content:space-between;padding-left:40px;font-family:"Montserrat",sans-serif;font-size:15px}
.stepper{width:36px;height:100%;border-left:1.5px solid #777;display:flex;align-items:center;justify-content:center}
.search-btn{position:absolute;left:92px;top:408px;width:146px;height:40px;border:1.5px solid var(--ink);font-family:"Montserrat",sans-serif;font-weight:700;font-size:17px;display:flex;align-items:center;justify-content:center}

/* welcome */
.welcome{position:absolute;left:0;top:780px;width:1200px;text-align:center}
.welcome-mark{width:60px;height:60px;border:2px solid var(--ink);margin:10px auto 0}
.welcome h1{font-weight:400;font-size:45px;margin-top:28px}
.welcome p{width:850px;margin:30px auto 0;font-size:15px;line-height:33px;color:#2a2a2a}

/* gallery */
.gallery{position:absolute;left:0;top:1190px;width:1200px;height:521px}
.gallery-bg{position:absolute;inset:0;background:linear-gradient(180deg,#2f3a33 0%,#45423a 50%,#2c2620 100%)}
.gallery h2{position:absolute;top:44px;width:100%;text-align:center;color:var(--white);font-weight:400;font-size:44px}
.thumb{position:absolute;top:142px;width:334px;height:208px;border:2px solid var(--white)}
.thumb-1{left:78px;background:linear-gradient(120deg,#e7e2da 0%,#d0c3ae 50%,#b22222 51%,#c6a87e 70%,#a78559 100%)}
.thumb-2{left:434px;background:linear-gradient(160deg,#ecebe6 0%,#dcdad3 50%,#c9c5bb 100%)}
.thumb-3{left:790px;background:linear-gradient(110deg,#8a1c1c 0%,#b03030 15%,#e8e6e2 35%,#d5d2cc 70%,#4b3a28 100%)}
.zoom{position:absolute;left:150px;top:88px}
.view-all{position:absolute;left:528px;top:411px;width:144px;height:40px;border:1.5px solid var(--white);color:var(--white);font-size:19px;display:flex;align-items:center;justify-content:center}

/* testimonials */
.testimonials{position:absolute;left:0;top:1740px;width:1200px;text-align:center}
.testimonials h2{font-weight:400;font-size:42px;margin-top:14px}
.quote-text{width:740px;margin:22px auto 0;font-size:13.5px;line-height:23px;color:var(--muted)}
.quote-mark{position:absolute;font-family:"Raleway",sans-serif;font-weight:700;font-size:110px;color:var(--quote);line-height:1}
.client-name{font-size:20px;margin-top:14px}
.avatar{width:86px;height:86px;border-radius:50%;margin:16px auto 0;border:3px solid #555;background:linear-gradient(180deg,#d8c6b0,#8a7a6a)}

/* contact */
.contact{position:absolute;left:0;top:2087px;width:1200px;height:461px}
.contact-bg{position:absolute;inset:0;background:linear-gradient(100deg,#4d4538 0%,#5a5448 40%,#3c3a36 70%,#2a2824 100%)}
.contact-panel{position:absolute;left:314px;top:61px;width:572px;height:332px;background:rgba(255,255,255,.32)}
.contact-panel h2{position:absolute;top:26px;width:100%;text-align:center;color:var(--white);font-weight:400;font-size:45px}
.icon-dot{flex:0 0 50px;width:50px;height:50px;border-radius:50%;background:#111;display:flex;align-items:center;justify-content:center}
.contact-row{position:absolute;display:flex;align-items:center;gap:12px;font-family:"Montserrat",sans-serif;font-weight:700;font-size:13px;color:#111;white-space:nowrap}
.row-address{left:28px;top:91px}
.row-phone{left:28px;top:166px}
.row-email{left:212px;top:166px}
.listings{position:absolute;left:151px;top:239px;display:flex;gap:22px}
.listing-badge{width:50px;height:50px;border-radius:50%;background:#111}

/* footer */
.site-footer{position:absolute;left:0;top:2548px;width:1200px;height:57px;background:var(--footer);color:var(--white);font-family:"Montserrat",sans-serif;font-size:15px;display:flex;align-items:center;justify-content:center}
.site-footer b{font-weight:700;margin:0 4px}
</style>
</head>
<body>

<header class="site-header">
  <div class="brand"><span class="brand-mark"></span>VILLA SERENO</div>
  <nav class="main-nav">
    <a class="active" href="#">HOME</a>
    <a href="#">ABOUT US</a>
    <a href="#">GALLERY</a>
    <a href="#">CONTECT US</a>
    <a href="#">AVAILABILITY</a>
  </nav>
</header>

<section class="hero">
  <div class="hero-photo" role="img" aria-label="Bright bedroom with a white bed, wooden wardrobe and arched window opening onto a balcony"></div>
  <svg class="hero-cut" viewBox="0 0 1200 714" width="1200" height="714">
    <polygon points="0,714 556,571 1200,601 1200,714" fill="#ffffff"/>
  </svg>
  <form class="booking">
    <h2>Book Your Stay</h2>
    <div class="field-label">Check In</div>
    <div class="date-field">DD MM YYYY
      <svg width="22" height="22" viewBox="0 0 22 22"><rect x="2" y="4" width="18" height="16" fill="none" stroke="#333" stroke-width="1.6"/><line x1="2" y1="9" x2="20" y2="9" stroke="#333" stroke-width="1.6"/><line x1="7" y1="2" x2="7" y2="6" stroke="#333" stroke-width="1.6"/><line x1="15" y1="2" x2="15" y2="6" stroke="#333" stroke-width="1.6"/><path d="M5 12h12M5 15h12M5 18h12M8 9v11M11 9v11M14 9v11" stroke="#333" stroke-width=".8"/></svg>
    </div>
    <div class="field-label">Check Out</div>
    <div class="date-field">DD MM YYYY
      <svg width="22" height="22" viewBox="0 0 22 22"><rect x="2" y="4" width="18" height="16" fill="none" stroke="#333" stroke-width="1.6"/><line x1="2" y1="9" x2="20" y2="9" stroke="#333" stroke-width="1.6"/><line x1="7" y1="2" x2="7" y2="6" stroke="#333" stroke-width="1.6"/><line x1="15" y1="2" x2="15" y2="6" stroke="#333" stroke-width="1.6"/><path d="M5 12h12M5 15h12M5 18h12M8 9v11M11 9v11M14 9v11" stroke="#333" stroke-width=".8"/></svg>
    </div>
    <div class="counts">
      <div>
        <div class="field-label">Adults</div>
        <div class="count-field">1<span class="stepper"><svg width="14" height="20" viewBox="0 0 14 20"><path d="M2 8l5-5 5 5M2 12l5 5 5-5" fill="none" stroke="#333" stroke-width="1.8"/></svg></span></div>
      </div>
      <div>
        <div class="field-label">Kids</div>
        <div class="count-field">1<span class="stepper"><svg width="14" height="20" viewBox="0 0 14 20"><path d="M2 8l5-5 5 5M2 12l5 5 5-5" fill="none" stroke="#333" stroke-width="1.8"/></svg></span></div>
      </div>
    </div>
    <div class="search-btn">SEARCH</div>
  </form>
</section>

<section class="welcome">
  <div class="welcome-mark"></div>
  <h1>Welcome to Villa Sereno</h1>
  <p>"Villa Sereno" is a newly renovated boutique 2-bedroom loft apartment in the historic centre of Florence (Firenze), Italy. "Villa Sereno" is perfectly located for your Tuscan holiday, offering easy walking access to all of central Florence - only 600m from the Duomo and Ponte Vecchio. The apartment is configured to sleep up to six and is furnished with elegant and luxury fittings, and has complimentary high-speed internet and cable-TV.</p>
</section>

<section class="gallery">
  <div class="gallery-bg" role="img" aria-label="Dimmed close-up of bathroom toiletry bottles"></div>
  <h2>Our Gallery</h2>
  <div class="thumb thumb-1" role="img" aria-label="Open-plan living area with a white staircase, red armchair and white dining chairs"></div>
  <div class="thumb thumb-2" role="img" aria-label="Loft bedroom with white bedding under a sloped ceiling">
    <svg class="zoom" width="34" height="34" viewBox="0 0 34 34"><circle cx="14" cy="14" r="9" fill="none" stroke="#111" stroke-width="4"/><line x1="21" y1="21" x2="30" y2="30" stroke="#111" stroke-width="5" stroke-linecap="round"/></svg>
  </div>
  <div class="thumb thumb-3" role="img" aria-label="Modern white kitchen with flowers on the dining table"></div>
  <div class="view-all">VIEW ALL</div>
</section>

<section class="testimonials">
  <h2>What Clients say</h2>
  <span class="quote-mark" style="left:156px;top:78px">“</span>
  <span class="quote-mark" style="left:990px;top:128px">”</span>
  <p class="quote-text">The location is perfect in the historic center, closed to everything. The apartment is just renovated and was perfect for our family of four(you can stay up to 6 I think). There was tons of really good restaurants outside on the street and also walking distance to the main train station(sm novella)</p>
  <div class="client-name">Marco Bellini</div>
  <div class="avatar" role="img" aria-label="Guest portrait"></div>
</section>

<section class="contact">
  <div class="contact-bg" role="img" aria-label="Dimmed living room with a sofa, dining table and radiator"></div>
  <div class="contact-panel">
    <h2>Keep In Touch</h2>
    <div class="contact-row row-address">
      <span class="icon-dot"><svg width="20" height="24" viewBox="0 0 20 24"><path d="M10 1C5 1 2 5 2 9c0 6 8 14 8 14s8-8 8-14c0-4-3-8-8-8z" fill="#fff"/><circle cx="10" cy="9" r="3" fill="#111"/></svg></span>
      Lorem Ipsum is simply dummy text of the printing.
    </div>
    <div class="contact-row row-phone">
      <span class="icon-dot"><svg width="22" height="22" viewBox="0 0 24 24"><path d="M6.6 10.8c1.4 2.8 3.8 5.1 6.6 6.6l2.2-2.2c.3-.3.7-.4 1-.2 1.1.4 2.3.6 3.6.6.6 0 1 .4 1 1V20c0 .6-.4 1-1 1C10.6 21 3 13.4 3 4c0-.6.4-1 1-1h3.5c.6 0 1 .4 1 1 0 1.3.2 2.5.6 3.6.1.3 0 .7-.2 1z" fill="#fff"/></svg></span>
      39 340 555 0182
    </div>
    <div class="contact-row row-email">
      <span class="icon-dot"><svg width="22" height="18" viewBox="0 0 22 18"><rect x="2" y="2" width="18" height="14" fill="none" stroke="#fff" stroke-width="1.8"/><path d="M2 3l9 7 9-7" fill="none" stroke="#fff" stroke-width="1.8"/></svg></span>
      reservations@villaserenostay.example
    </div>
    <div class="listings">
      <span class="listing-badge"></span>
      <span class="listing-badge"></span>
      <span class="listing-badge"></span>
      <span class="listing-badge"></span>
    </div>
  </div>
</section>

<footer class="site-footer">© <b>VillaSereno</b> - 2016. All Rights Reserved.</footer>

</body>
</html>
```